Website for Youth Orchestra to sell tickets and attract young musicians

We are looking for a new website design for a Youth Orchestra; one of the best classical youth orchestras in the county. This project is the design only. <br/><br/>The website serves two main purposes:<br/>• Selling tickets for concerts and performances of the orchestra<br/>• Recruiting young musicians to do audition for the orchestra<br/>
Updates

Need extra days to review

Target Market(s)

Classical music lovers with a special interest in young upcoming musicians.
Young talented musicians

Number of Pages Required

2 page

Colors
ec1f27

Requirements
Must have
• - A Picture on the front page that promotes the main upcomming event
• - Attention for recruiting new musicians
• - Pictures with young musicians (white back ground, see examples)
• - Responsive
• - Please use the logo attached
Should not have
• The brown colors of the current website (kvb-velmorin.example)

```html
<!DOCTYPE html>
<html lang="en">
<head>
<meta charset="utf-8">
<title>Velmorin Jeugd Orkest</title>
<link href="https://fonts.googleapis.com/css2?family=Roboto:wght@300;400;500;700&display=swap" rel="stylesheet">
<style>
:root{
  --brand:#ec1f27;
  --ink:#111;
  --hero-bg:#05040c;
  --footer-bg:#7a1a1b;
  --grey:#5e5e5e;
  --text-muted:#555;
  --white:#fff;
}
*{box-sizing:border-box;margin:0;padding:0}
html,body{width:972px;height:1200px;overflow:hidden;background:var(--white);font-family:"Roboto",sans-serif;color:var(--ink)}
.page{position:relative;width:972px;height:1200px}
.abs{position:absolute}

/* hero */
.hero{position:absolute;left:0;top:0;width:972px;height:434px;background:var(--hero-bg);overflow:hidden}
.hero-photo{position:absolute;left:0;top:0;width:972px;height:434px;
  background:
    radial-gradient(ellipse 130px 110px at 600px 150px,rgba(120,90,235,.85) 0%,rgba(90,60,210,.45) 55%,rgba(5,4,12,0) 100%),
    radial-gradient(ellipse 120px 90px at 840px 300px,rgba(110,80,220,.7) 0%,rgba(60,40,160,.3) 60%,rgba(5,4,12,0) 100%),
    radial-gradient(ellipse 190px 45px at 640px 275px,rgba(140,55,25,.75) 0%,rgba(90,30,20,.35) 60%,rgba(5,4,12,0) 100%),
    radial-gradient(ellipse 330px 230px at 690px 210px,rgba(45,30,130,.85) 0%,rgba(25,15,80,.5) 55%,rgba(5,4,12,0) 100%),
    var(--hero-bg)}
.brand-disc{position:absolute;left:122px;top:-91px;width:182px;height:182px;border-radius:50%;background:var(--brand);
  display:flex;align-items:flex-end;justify-content:center;padding-bottom:24px;color:var(--white);
  font-weight:500;font-size:18px;line-height:1.1;text-align:center}
.nav{position:absolute;left:320px;top:28px;display:flex;gap:10px;font-size:8px;font-weight:700;color:var(--white);white-space:nowrap}
.nav .current{color:#aaa;font-weight:500}
.nav-rule{position:absolute;left:320px;top:48px;width:652px;height:1px;background:#333}
.headline{color:var(--white);font-weight:300;line-height:1;white-space:nowrap}
.h-offering{left:160px;top:106px;font-size:23px;letter-spacing:.5px}
.h-young{left:118px;top:142px;font-size:62px;letter-spacing:-1px}
.h-young small{font-size:38px;letter-spacing:0}
.h-musicians{left:140px;top:210px;font-size:22px}
.h-play{left:154px;top:248px;font-size:62px}
.h-play small{font-size:36px}
.h-orch{left:155px;top:313px;font-size:39px}
.h-orch small{font-size:10px}
.h-years{left:264px;top:360px;font-size:62px}
.h-years small{font-size:14px}
.login{left:735px;top:401px;font-size:8.5px;font-weight:700;color:var(--white);text-decoration:underline}
.btn{display:flex;align-items:center;justify-content:center;border-radius:30px;color:var(--white);font-weight:500}
.btn-register{left:772px;top:394px;width:78px;height:25px;background:var(--brand);font-size:8.5px}

/* concerts */
.arrow{top:648px;width:14px;height:24px}
.card{top:477px;width:243px;height:384px;background:var(--white);box-shadow:0 1px 8px rgba(0,0,0,.15);border-radius:3px}
.card-title{position:absolute;left:0;top:5px;width:100%;text-align:center;font-size:15px;line-height:18px;font-weight:400;text-transform:uppercase}
.card-media{position:absolute;left:12px;top:45px;width:219px;height:222px}
.media-poster{background:
  radial-gradient(ellipse 70px 55px at 150px 100px,rgba(240,110,60,.85) 0%,rgba(240,110,60,0) 100%),
  radial-gradient(ellipse 40px 45px at 35px 85px,rgba(70,50,130,.6) 0%,rgba(70,50,130,0) 100%),
  linear-gradient(180deg,#e4d3ea 0%,#dcc7e4 100%)}
.media-choir{background:
  radial-gradient(ellipse 110px 70px at 110px 70px,rgba(200,165,100,.7) 0%,rgba(200,165,100,0) 100%),
  linear-gradient(180deg,#6d5a3b 0%,#9a7f52 35%,#5d5148 58%,#2e2c2e 75%,#8d8580 100%)}
.program{position:absolute;left:12px;top:274px;width:222px;font-size:5.8px;line-height:7.9px;font-weight:300;color:var(--text-muted)}
.program strong{display:block;font-size:8.3px;line-height:10px;font-weight:400;color:var(--ink)}
.program .more{color:var(--brand)}
.date{position:absolute;left:13px;top:340px;color:var(--brand);font-weight:700;font-size:9.2px;line-height:11px}
.date b{display:block;font-size:15px;line-height:17px}
.card .btn{position:absolute;left:117px;top:343px;width:112px;height:33px;font-size:10.5px}
.btn-tickets{background:var(--brand)}
.btn-soldout{background:var(--grey)}
.divider{left:722px;top:477px;width:1px;height:392px;background:#c8c8c8}
.sponsor{left:736px;width:116px;height:117px;border:1px solid var(--brand);display:flex;flex-direction:column;align-items:center;justify-content:center;gap:8px;text-align:center;font-size:11px;color:#333}
.sponsor .mark{width:40px;height:40px;background:var(--brand)}
.sponsor .mark.round{border-radius:50%;background:#f08a24}

/* footer */
.footer{position:absolute;left:0;top:914px;width:972px;height:286px;background:var(--footer-bg);border-top:2px solid var(--brand)}
.footer-photo{position:absolute;left:0;top:0;width:300px;height:284px;
  background:
    radial-gradient(ellipse 70px 90px at 120px 80px,rgba(215,110,100,.55) 0%,rgba(215,110,100,0) 100%),
    radial-gradient(ellipse 160px 120px at 110px 200px,rgba(200,80,75,.5) 0%,rgba(200,80,75,0) 100%),
    linear-gradient(90deg,#a8302e 0%,#962826 60%,rgba(122,26,27,0) 100%)}
.footer-links{position:absolute;left:312px;top:61px;list-style:none;font-size:9.8px;line-height:15.8px;color:var(--white)}
.footer-heading{font-size:8.5px;color:var(--white);font-weight:700}
.contact{left:455px;top:60px}
.contact p{font-size:7.8px;line-height:15.8px;color:var(--white)}
.social{left:455px;top:1px;top:160px;display:flex;gap:8px;font-size:6.5px;color:var(--white)}
.social span{display:flex;align-items:center;gap:2px}
.social i{display:block;width:10px;height:10px;border-radius:50%;background:var(--white)}
.news{left:634px;top:60px;width:200px}
.news .footer-heading{font-weight:400}
.news p{margin-top:12px;font-size:6.8px;line-height:15.8px;color:var(--white)}
.email{left:634px;top:118px;width:186px;height:24px;background:#a81c20;border:1px solid #c23a3c;color:var(--white);font-size:7px;padding:7px 10px}
.btn-submit{left:634px;top:155px;width:69px;height:24px;background:var(--brand);font-size:7.5px;font-weight:400}
</style>
</head>
<body>
<div class="page">

  <header class="hero">
    <div class="hero-photo" role="img" aria-label="Photo of a young violinist playing, lit in violet stage light"></div>
    <div class="brand-disc">Velmorin<br>Jeugd Orkest</div>
    <nav class="nav">
      <span class="current">HOME</span><span>ORCHESTRA</span><span>PLAY ALONG</span><span>CONCERTS</span><span>TOURS</span><span>PARTNERS</span><span>FRIENDS</span><span>FORMER MEMBERS</span><span>CONTACT &amp; ORGANIZATION</span>
    </nav>
    <div class="nav-rule"></div>
    <div class="abs headline h-offering">OFFERING</div>
    <div class="abs headline h-young">YOUNG <small>TALENTED</small></div>
    <div class="abs headline h-musicians">MUSICIANS THE OPPORTUNITY</div>
    <div class="abs headline h-play"><small>TO</small> PLAY</div>
    <div class="abs headline h-orch"><small>IN A LARGE</small> SYMPHONY ORCHESTRA</div>
    <div class="abs headline h-years"><small>FOR</small> 57 <small>YEARS</small></div>
    <a class="abs login">LOG IN</a>
    <a class="abs btn btn-register">REGISTER</a>
  </header>

  <svg class="abs arrow" style="left:120px" viewBox="0 0 14 24"><path d="M11 2 2 12l9 10" fill="none" stroke="#ec1f27" stroke-width="1.6"/></svg>
  <svg class="abs arrow" style="left:697px" viewBox="0 0 14 24"><path d="M3 2l9 10-9 10" fill="none" stroke="#ec1f27" stroke-width="1.6"/></svg>

  <article class="abs card" style="left:164px">
    <h2 class="card-title">VJO New Year’s Concert</h2>
    <div class="card-media media-poster" role="img" aria-label="Concert poster illustration with an orange glass and coloured bubbles"></div>
    <div class="program">
      <strong>Program:</strong>
      Pieter Holsbeek (1862-1941) ~ The Doge of Venice Op. 20 (1908)<br>
      Lucien Marchetti (1835-1921) ~ Morceau de concert horn &amp; orchestra, Op. 94 (1887)<br>
      Soloist: Joris van Dael (from his own orchestra)<br>
      Tomas Vranek (1841-1904) ~ Three volumes from: Symphony No. 8 in G major, Op. 88 (1889)<br>
      <span class="more">Read more »</span>
    </div>
    <div class="date"><b>Sunday</b>January 12, 2020<br>14:30</div>
    <a class="btn btn-tickets">TICKETS</a>
  </article>

  <article class="abs card" style="left:431px">
    <h2 class="card-title">Lindel Consort + Cantori Nova<br>concert with VJO</h2>
    <div class="card-media media-choir" role="img" aria-label="Photo of the orchestra and choir performing in a church"></div>
    <div class="program">
      <strong>Program:</strong>
      Vranek - parts of Symphony No. 8 in G on.. 88 (orchestra)<br>
      Adler - Two motets on. 74 (choirs)<br>
      Reinhart - Mass in C major op. 86<br>
      mmv soloists: Mirte Koning - soprano, Elke Voorn - alto, Sander Brink - tenor and Ruben Hartog - bass<br>
      <span class="more">Read more »</span>
    </div>
    <div class="date"><b>Sunday</b>November 24, 2019<br>3.30 pm</div>
    <a class="btn btn-soldout">SOLD OUT</a>
  </article>

  <div class="abs divider"></div>
  <div class="abs sponsor" style="top:477px"><div class="mark"></div>HAVENSTAD<br>KLASSIEK</div>
  <div class="abs sponsor" style="top:615px"><div class="mark"></div>NIMBUS RELAY</div>
  <div class="abs sponsor" style="top:752px"><div class="mark round"></div>Veldhof Bank</div>

  <footer class="footer">
    <div class="footer-photo" role="img" aria-label="Photo of a young violinist, tinted red"></div>
    <ul class="footer-links">
      <li>commissions</li><li>conductor</li><li>code of conduct</li><li>orchestra members</li><li>audit data</li><li>audition form</li><li>visit rehearsal</li><li>vacancies</li>
    </ul>
    <div class="abs contact">
      <div class="footer-heading">CONTACT US</div>
      <p style="margin-top:8px">Velmorin Jeugd Orkest<br>Postbus 412<br>4100KM Velmorin</p>
    </div>
    <div class="abs social"><span><i></i>Share</span><span><i></i>Post</span><span><i></i>Watch</span></div>
    <div class="abs news">
      <div class="footer-heading">SUBSCRIBE TO OUR NEWSLETTER</div>
      <p>Subscribe to our newsletter to stay up to date with the<br>latest news and offers</p>
    </div>
    <div class="abs email">Enter your email address</div>
    <a class="abs btn btn-submit">SUBMIT</a>
  </footer>
</div>
</body>
</html>
```